Letterbox flyer design

Hi - hoping you're able to help design a flyer for letterbox delivery. I think it needs to be 99mm x 210mm.

Side 1 - Large Logo, dark back ground.
Larger text - "5%* Property Management."
Medium Text - "Better Services, Lower Fee's, Higher Yields"
Smaller text at bottom - "0472 519 084 - gideon@pellbrook.com.au - pellbrook.com.au"

Back Side -
• Management Fee – 5%+GST of rent collected (no rent paid = no mgmt. fee charged)
• An Establishment fee of $500 for new tenancies we establish.
• Marketing Costs as Required and agreed to between parties.
• No Fee’s for Condition Reports, inspections, re-listing, tenancy renewal, admin costs, or any other ‘sundry’ charges.
• All rent is paid out monthly, yearly ‘profit-and-loss’ statements at no cost.
• Ingoing condition report is produced prior to occupancy, and routine condition inspections are conducted after the first 3months, then every 6months.
• Open homes are advertised in advance, and held on the weekend and one lunchtime or evening per week.
• All applicants are vetted, with the most suitable sent through for your consideration and approval.
• Advise on different tenancy terms as they could have the ability to affect the long-term yields.

```html
<!DOCTYPE html>
<html lang="en">
<head>
<meta charset="utf-8">
<title>Pellbrook &amp; Co – Property Management Flyer</title>
<link href="https://fonts.googleapis.com/css2?family=Outfit:wght@500;600;700&display=swap" rel="stylesheet">
<style>
  :root {
    --stage: #4b4b4b;
    --ink: #222121;
    --teal: #42bec7;
    --grey: #8a8a8a;
    --white: #ffffff;
  }
  html, body {
    margin: 0;
    width: 1200px;
    height: 1200px;
    overflow: hidden;
    background: var(--stage);
    font-family: "Outfit", sans-serif;
  }
  .flyer {
    position: absolute;
    left: 356px;
    top: 84px;
    width: 486px;
    height: 1030px;
    background: var(--ink);
    overflow: hidden;
  }
  .flyer-shapes {
    position: absolute;
    inset: 0;
  }
  .brand {
    position: absolute;
    left: 0;
    top: 46px;
    width: 314px;
    text-align: center;
    color: var(--grey);
    font-weight: 700;
    text-transform: uppercase;
    line-height: 1;
  }
  .brand-ring {
    width: 146px;
    height: 146px;
    margin: 0 auto 18px;
    border: 3px solid var(--teal);
    border-radius: 50%;
    box-sizing: border-box;
  }
  .brand-name {
    font-size: 36px;
    letter-spacing: 0.5px;
  }
  .brand-sub {
    font-size: 25px;
    margin-top: 6px;
  }
  .offer {
    position: absolute;
    left: 42px;
    top: 312px;
    color: var(--teal);
    font-weight: 600;
    font-size: 148px;
    line-height: 1;
    letter-spacing: -3px;
  }
  .offer sup {
    font-size: 100px;
    vertical-align: top;
    position: relative;
    top: -6px;
    margin-left: 4px;
  }
  .service {
    position: absolute;
    left: 42px;
    top: 452px;
    margin: 0;
    color: var(--grey);
    font-weight: 600;
    font-size: 50px;
    line-height: 44px;
    text-transform: uppercase;
  }
  .benefits {
    position: absolute;
    left: 44px;
    top: 552px;
    margin: 0;
    padding: 0;
    list-style: none;
    color: var(--teal);
    font-weight: 600;
    font-size: 26px;
    line-height: 35.5px;
    text-transform: uppercase;
  }
  .benefits li::before {
    content: "";
    display: inline-block;
    width: 8px;
    height: 8px;
    background: var(--teal);
    margin-right: 18px;
    vertical-align: middle;
    position: relative;
    top: -3px;
  }
  .city-photo {
    position: absolute;
    left: 0;
    top: 678px;
    width: 486px;
    height: 176px;
    background: linear-gradient(180deg, #d9a46a 0%, #7f7a82 35%, #3d4a52 70%, #6c8aa0 100%);
  }
  .contact-band {
    position: absolute;
    left: 0;
    top: 852px;
    width: 486px;
    height: 178px;
    background: var(--teal);
  }
  .phone {
    position: absolute;
    left: 46px;
    top: 814px;
    width: 400px;
    height: 76px;
    border-radius: 38px;
    background: var(--ink);
    color: var(--white);
    display: flex;
    align-items: center;
    justify-content: center;
    gap: 6px;
    font-weight: 600;
    font-size: 50px;
  }
  .phone svg { width: 18px; height: 24px; }
  .email {
    position: absolute;
    left: 0;
    top: 898px;
    width: 486px;
    text-align: center;
    color: var(--ink);
    font-weight: 500;
    font-size: 28px;
  }
  .website {
    position: absolute;
    left: 0;
    top: 940px;
    width: 486px;
    text-align: center;
    color: var(--ink);
    font-weight: 700;
    font-size: 27px;
    letter-spacing: 4px;
    text-transform: uppercase;
  }
</style>
</head>
<body>
  <main class="flyer">
    <svg class="flyer-shapes" viewBox="0 0 486 1030" width="486" height="1030">
      <polygon class="corner-accent" points="280,0 486,0 486,94 428,148" fill="var(--teal)"/>
      <polygon class="keys-photo" role="img" aria-label="Black and white photo of a hand holding house keys"
               points="316,150 486,94 486,322" fill="#9a9a9a"/>
      <polygon class="mid-accent" points="344,322 486,322 486,444" fill="var(--teal)"/>
    </svg>

    <div class="brand">
      <div class="brand-ring"></div>
      <div class="brand-name">Pellbrook &amp; Co</div>
      <div class="brand-sub">Property Services</div>
    </div>

    <div class="offer">5%<sup>*</sup></div>
    <h1 class="service">Property<br>Management</h1>

    <ul class="benefits">
      <li>Better Services</li>
      <li>Lower Fee's</li>
      <li>Higher Yields</li>
    </ul>

    <div class="city-photo" role="img" aria-label="City waterfront apartment towers at dusk"></div>
    <div class="contact-band"></div>

    <div class="phone">
      <svg viewBox="0 0 12 16" aria-hidden="true"><path d="M4 1 L6 4 L4.5 6 Q5 9 7.5 11 L9.5 9.5 L11.5 12 L9.5 14.5 Q2 12 1.5 3 Z" fill="var(--white)"/></svg>
      <span>0472 519 084</span>
    </div>
    <div class="email">gideon@pellbrook.com.au</div>
    <div class="website">pellbrook.com.au</div>
  </main>
</body>
</html>
```